Business Card for KRB Farmhaul

Custom Business Card Brief:
1. We need two designs for this single client, KRB Farmhaul LLC and both designs will end up with rounded corner printed cards that fit the ZIVA.com design format for their special printing style.
2. My client needs two separate card designs since half of their target market is for farm owners in the Cattle and Beef world. The other half of their target market is working with Equine aka Horse farm owners.
3. The look for two card designs can be similar to ensure branding consistency but we will need some space sizing differences so the cards stand out differently in regards to how the services mentioned are laid out on the front of each card design.
4. Both card designs require the front of the card holding all of the great design work. The back of these 2-sided cards will remain white and can just have the contact information listed "again" on the back to match the contact information provided on the front.
5. Card Design 1 will be for Equine customers, Card Design 2 will be for his Cattle/Beef customers.
6. Card Design 1 (Equine) we are thinking we set aside 70% of the card to be dedicated to the Services listed section while the remaining 30% of the front of the card space will hold a smaller logo image space along with his name and contact information.
7. Card Design 2 (Cattle/Beef) we will need opposite of my last point. We want 70% of the card dedicated to a larger logo space and his contact information while the remaining 30% listing the services provided.
8. Card Design #1 - Equine - his Services space should include:
- Equine Mortality Services
- General Removal
- Cremation
- Transportation for Necropsy
9. Card Design #2 - Cattle/Beef - his Services space should include: General Livestock Services, Hauling, Order Buying, Dealing, Dead Stock Removal
10. Contact Information for both card designs:
- Dennis R. Hollorand (owner)
- KRB Farmhaul LLC (company)
- 608-413-5972 (phone)
- info@krbfarmhaulgroup.example (email)
- KRBFarmhaulGroup.example (website)
11. Additional Branding Details - The color codes aka pantone colors that are in the current logo file design:
- Blue Pantone 7686C
- Grey Pantone 422C
12. The font styles used in the logo:
- Nexa Bold
- Nexa Rust Slab Black Shadow
13. Back of both card designs, just list his contact information in larger size to stand out more on the white back:
- 608-413-5972 (phone)
Updates

Okay thanks for confirming that our final design files will be ready for the ZIVA.com format. I noticed the 2nd place vertical card already had rounded corners but the horizontal design that was in 1st place still had sharp square corners. When using the ZIVA.com format we will be rounding all of the corners of both cards for print. So we just wanted to make sure that both sets of files will be in a rounded design meeting their format sizing to ensure no content from your great designs gets cut off. Thank you again for your attention to detail. ~ Glenn

Target Market(s)

Business to Business

Industry/Entity Type

Farming, Agriculture, Livestock

Contact Information for Business Card

Clients' logo, his contact info, and his different services on two similar final card designs.

Font styles to use
Other font styles liked:
• Look at the brief to see how his logo fonts are currently.

Requirements
Must have
• Two versions of the card, one for the Equine horse market, and one for the Cattle/Beef market of farming.
Nice to have
• Clean, sharp, concise.
Should not have
• No flashy or cartoony designs.

```html
<!DOCTYPE html>
<html lang="en">
<head>
<meta charset="utf-8">
<title>KRB Farmhaul – Business Cards</title>
<link rel="stylesheet" href="https://fonts.googleapis.com/css2?family=Montserrat:wght@500;600;700&display=swap">
<style>
  :root {
    --bg: #d9d7d5;
    --navy: #173a5e;
    --grey: #6f7780;
    --stripe-blue: #2c56a3;
    --stripe-grey: #8e9399;
    --card-white: #f4f4f4;
    --dark: #050505;
    --divider: rgba(255,255,255,0.45);
  }
  * { box-sizing: border-box; margin: 0; padding: 0; }
  html, body { width: 1200px; height: 1200px; overflow: hidden; }
  body {
    background: var(--bg);
    font-family: "Montserrat", sans-serif;
    position: relative;
  }
  .card {
    position: absolute;
    left: 243px;
    width: 702px;
    height: 400px;
    border-radius: 22px;
    overflow: hidden;
    background: var(--card-white);
  }
  .card--front { top: 170px; }
  .card--back { top: 630px; background: linear-gradient(135deg, #fafafa 0%, #ececec 60%, #e2e2e2 100%); }

  /* Front – contact column */
  .contact-column {
    position: absolute; left: 0; top: 0; width: 253px; height: 100%;
    text-align: center; color: var(--navy);
  }
  .brand-mark {
    position: absolute; top: 82px; left: 0; width: 100%;
    display: flex; align-items: center; justify-content: center; gap: 8px;
  }
  .brand-mark__dot { width: 14px; height: 14px; border-radius: 50%; background: var(--navy); }
  .brand-mark__name { font-weight: 700; font-size: 20px; color: var(--navy); }
  .person-name { position: absolute; top: 204px; width: 100%; font-weight: 600; font-size: 15px; }
  .person-role { position: absolute; top: 224px; width: 100%; font-weight: 500; font-size: 13px; color: var(--grey); letter-spacing: 0.5px; }
  .icon-row { position: absolute; top: 290px; width: 100%; display: flex; justify-content: center; gap: 4px; }
  .icon-row svg { width: 17px; height: 17px; }
  .contact-line { position: absolute; width: 100%; font-weight: 600; font-size: 12.5px; }
  .contact-line--phone { top: 316px; font-size: 13.5px; }
  .contact-line--email { top: 337px; font-size: 11.8px; }
  .contact-line--web { top: 358px; }

  .divider-stripe {
    position: absolute; left: 253px; top: 0; width: 6px; height: 100%;
    background: linear-gradient(180deg, var(--stripe-grey) 0%, var(--stripe-grey) 45%, var(--stripe-blue) 100%);
  }

  /* Front – services panel */
  .services-panel {
    position: absolute; left: 259px; top: 0; right: 0; height: 100%;
    background: var(--dark); color: #fff;
  }
  .services-panel__decor {
    position: absolute; left: 40px; top: 60px; width: 380px; height: 330px;
    background: radial-gradient(ellipse at 55% 50%, rgba(70,70,70,0.35) 0%, rgba(30,30,30,0.15) 50%, rgba(0,0,0,0) 75%);
  }
  .service {
    position: absolute; left: 0; width: 100%; text-align: center;
    font-weight: 600; font-size: 22px; line-height: 40px;
  }
  .service-rule {
    position: absolute; left: 130px; width: 210px; height: 1px;
    background: linear-gradient(90deg, transparent, var(--divider), transparent);
  }

  /* Back */
  .back-company { position: absolute; top: 34px; width: 100%; text-align: center; color: var(--navy); font-weight: 700; font-size: 31px; letter-spacing: -0.5px; }
  .back-company small { font-size: 15px; font-weight: 600; }
  .back-name { position: absolute; top: 96px; width: 100%; text-align: center; color: var(--navy); font-weight: 600; font-size: 26px; }
  .back-role { position: absolute; top: 130px; width: 100%; text-align: center; color: var(--grey); font-weight: 500; font-size: 21px; letter-spacing: 0.5px; }
  .back-icon-row { position: absolute; top: 187px; left: 0; width: 100%; display: flex; justify-content: center; align-items: center; gap: 12px; }
  .back-icon-row .rule { width: 125px; height: 3px; background: var(--navy); margin: 0 8px; }
  .back-icon-row svg { width: 38px; height: 38px; }
  .back-line { position: absolute; width: 100%; text-align: center; color: var(--navy); font-weight: 600; font-size: 21px; }
  .back-line--phone { top: 258px; font-size: 22px; }
  .back-line--email { top: 296px; }
  .back-line--web { top: 336px; }
</style>
</head>
<body>

<svg width="0" height="0" style="position:absolute" aria-hidden="true">
  <defs>
    <symbol id="icon-phone" viewBox="0 0 40 40">
      <circle cx="20" cy="20" r="20" fill="#173a5e"/>
      <path d="M14 10c1-.6 2-.4 2.6.5l2 3.3c.5.8.3 1.8-.4 2.4l-1.5 1.2c1 2.4 2.8 4.3 5.2 5.4l1.3-1.5c.6-.7 1.6-.8 2.4-.3l3.3 2c.9.6 1.1 1.7.5 2.6l-1.2 1.8c-.7 1-2 1.5-3.2 1.2C18.7 27.2 12.8 21.3 11.4 15c-.3-1.2.2-2.4 1.2-3.2z" fill="#fff"/>
    </symbol>
    <symbol id="icon-mail" viewBox="0 0 40 40">
      <circle cx="20" cy="20" r="20" fill="#173a5e"/>
      <rect x="10" y="13" width="20" height="14" rx="1.5" fill="none" stroke="#fff" stroke-width="2"/>
      <path d="M10.5 14l9.5 7.5 9.5-7.5" fill="none" stroke="#fff" stroke-width="2"/>
    </symbol>
    <symbol id="icon-web" viewBox="0 0 40 40">
      <circle cx="20" cy="20" r="20" fill="#173a5e"/>
      <circle cx="20" cy="20" r="10.5" fill="none" stroke="#fff" stroke-width="1.8"/>
      <ellipse cx="20" cy="20" rx="4.5" ry="10.5" fill="none" stroke="#fff" stroke-width="1.8"/>
      <path d="M9.5 20h21M11 15h18M11 25h18" stroke="#fff" stroke-width="1.6"/>
    </symbol>
  </defs>
</svg>

<section class="card card--front" aria-label="Equine card front">
  <div class="contact-column">
    <div class="brand-mark">
      <span class="brand-mark__dot"></span>
      <span class="brand-mark__name">KRB Farmhaul</span>
    </div>
    <p class="person-name">Dennis R. Hollorand</p>
    <p class="person-role">Owner</p>
    <div class="icon-row">
      <svg><use href="#icon-phone"/></svg>
      <svg><use href="#icon-mail"/></svg>
      <svg><use href="#icon-web"/></svg>
    </div>
    <p class="contact-line contact-line--phone">608-413-5972</p>
    <p class="contact-line contact-line--email">info@krbfarmhaulgroup.example</p>
    <p class="contact-line contact-line--web">KRBFarmhaulGroup.example</p>
  </div>

  <div class="divider-stripe"></div>

  <div class="services-panel">
    <div class="services-panel__decor" role="img" aria-label="Faint outline of a horse head as a background decoration"></div>
    <p class="service" style="top:37px">Equine Mortality Services</p>
    <div class="service-rule" style="top:104px"></div>
    <p class="service" style="top:120px">General Removal</p>
    <div class="service-rule" style="top:182px"></div>
    <p class="service" style="top:200px">Cremation</p>
    <div class="service-rule" style="top:267px"></div>
    <p class="service" style="top:280px">Transportation for</p>
    <p class="service" style="top:319px">Necropsy</p>
  </div>
</section>

<section class="card card--back" aria-label="Card back">
  <h1 class="back-company">KRB FARMHAUL <small>LLC</small></h1>
  <p class="back-name">Dennis R. Hollorand</p>
  <p class="back-role">Owner</p>
  <div class="back-icon-row">
    <span class="rule"></span>
    <svg><use href="#icon-phone"/></svg>
    <svg><use href="#icon-mail"/></svg>
    <svg><use href="#icon-web"/></svg>
    <span class="rule"></span>
  </div>
  <p class="back-line back-line--phone">608-413-5972</p>
  <p class="back-line back-line--email">info@krbfarmhaulgroup.example</p>
  <p class="back-line back-line--web">KRBFarmhaulGroup.example</p>
</section>

</body>
</html>
```